TV Media buying firm needs Lead Gen page layout

We need a landing page using our current website look and feel to capture leads from our Chatterleaf ads. A quick form to capture Name, phone number, email, and a short message.
The call to action button should state "Get a free direct response campaign audit now!"
Updates

please visit www.brantlowmedia.com for the look and feel of the landing page.

I also uploaded a screenshot of what kind of landing page we are looking for.
the image has been reduced to 50% for the overall view.
thanks!

Please use our website's look and feel as reference for colors, fonts,header and footers.

The video placement on the sample file can be an image or combination image & text.

Again, please reference www.brantlowmedia.com for the look and feel.

Target Market(s)

50+ Market, Cheif Marketing Officer, Summit 1000 Companies

Industry/Entity Type

Tv

```html
<!DOCTYPE html>
<html lang="en">
<head>
<meta charset="utf-8">
<title>Brantlow Media – Direct Response Marketing Agency</title>
<link href="https://fonts.googleapis.com/css2?family=Arimo:wght@400;700&family=Roboto+Condensed:wght@700&display=swap" rel="stylesheet">
<style>
:root{
  --red:#c8141c;
  --red-dark:#a30f16;
  --red-light:#e02a30;
  --ink:#1f1f1f;
  --text:#4a4a4a;
  --muted:#7a7a7a;
  --line:#dcdcdc;
  --strip:#e4e4e4;
  --topbar:#2b2b2b;
  --footer:#1b1b1c;
  --footer-text:#8d8d8d;
  --white:#ffffff;
  --icon:#6b6b6b;
}
*{box-sizing:border-box;margin:0;padding:0}
html,body{width:992px;height:1200px;overflow:hidden}
body{position:relative;background:var(--white);font-family:"Arimo",Arial,sans-serif;color:var(--text)}
.abs{position:absolute}

/* top strip */
.top-strip{left:0;top:0;width:992px;height:24px;background:var(--topbar);color:#e8e8e8;font-size:10.5px;line-height:24px;padding-left:88px}

/* header */
.site-header{left:0;top:24px;width:992px;height:68px;background:linear-gradient(#ffffff,#f1f1f1)}
.brand{left:88px;top:17px;display:flex;align-items:center;gap:9px}
.brand-mark{width:14px;height:14px;background:var(--red);display:block}
.brand-name{font-size:24px;font-weight:700;color:var(--ink);line-height:28px}
.social{left:612px;top:10px;display:flex;gap:6px}
.social span{width:10px;height:10px;border-radius:50%;background:#9a9a9a;display:block}
.contact{left:730px;top:6px;font-size:15px;font-weight:700;color:var(--ink)}
.contact b{color:var(--red)}
.main-nav{right:87px;top:37px;display:flex;font-size:10.5px;color:var(--ink)}
.main-nav a{color:inherit;text-decoration:none;padding:4px 10px;line-height:11px}
.main-nav a.current{background:var(--red);color:var(--white)}

/* hero */
.hero{left:0;top:92px;width:992px;height:369px;background:radial-gradient(ellipse at 50% 40%,var(--red-light) 0%,var(--red) 55%,var(--red-dark) 100%)}
.hero-arrow{top:150px}
.video{left:89px;top:39px;width:470px;height:294px;background:#111}
.video-frame{left:0;top:0;width:470px;height:273px;background:linear-gradient(135deg,#3a3a3a 0%,#6f6f6f 40%,#c9b08a 70%,#3c3c3c 100%)}
.video-bar{left:0;top:273px;width:470px;height:21px;background:#1a1a1a}
.video-bar .progress{position:absolute;left:0;top:0;width:470px;height:3px;background:#555}
.video-bar .progress i{display:block;width:20px;height:3px;background:var(--red)}
.video-time{position:absolute;left:50px;top:7px;font-size:8px;color:#ddd}

.lead-form{left:606px;top:38px;width:294px;height:297px}
.form-head{left:0;top:0;width:294px;height:53px;background:#1f1f1f;color:var(--white);font-family:"Roboto Condensed",Arial,sans-serif;font-size:21px;line-height:20px;padding:9px 0 0 22px}
.form-body{left:6px;top:53px;width:282px;height:244px;background:var(--white)}
.field{position:absolute;left:39px;width:222px;height:26px;border:1px solid #cfcfcf;border-radius:2px;font-size:10px;color:#9b9b9b;padding:7px 0 0 6px}
.field-icon{position:absolute;left:20px}
.cta{position:absolute;left:20px;top:193px;width:240px;height:34px;background:var(--red);color:var(--white);font-family:"Roboto Condensed",Arial,sans-serif;font-size:12.5px;text-align:center;line-height:32px;border-bottom:2px solid var(--red-dark)}

/* client strip */
.client-strip{left:0;top:461px;width:992px;height:78px;background:var(--strip)}
.client{position:absolute;top:29px;transform:translateX(-50%);font-size:17px;font-weight:700;color:#5a5a5a;white-space:nowrap;display:flex;align-items:center;gap:5px}
.client i{display:block;width:10px;height:10px;background:#5a5a5a;border-radius:50%}

/* services */
.section-title{left:0;top:568px;width:992px;text-align:center;font-size:19.5px;font-weight:700;color:var(--red)}
.service-title{font-size:12.5px;font-weight:700;color:var(--ink);white-space:nowrap}
.service-text{font-size:10.2px;line-height:12.6px;color:var(--text);width:186px}
.service-icon{width:24px;height:26px}
.rule-h{height:1px;background:var(--line)}
.rule-v{width:1px;background:var(--line)}

/* footer */
.site-footer{left:0;top:1092px;width:992px;height:108px;background:var(--footer);color:var(--footer-text);text-align:center;font-size:7.8px;line-height:12.4px;padding-top:20px}
.site-footer .marks{margin-top:8px}
</style>
</head>
<body>

<div class="abs top-strip">DRTV, Media Buying, Direct Response Television, DRTV Advertising, World Class Media Buying Agency - Brantlow Media</div>

<header class="abs site-header">
  <div class="abs brand">
    <span class="brand-mark" aria-hidden="true"></span>
    <span class="brand-name">Brantlow Media</span>
  </div>
  <div class="abs social" aria-hidden="true"><span></span><span></span><span></span><span></span><span></span><span></span><span></span></div>
  <div class="abs contact">Contact Us: <b>214-555-0186</b></div>
  <nav class="abs main-nav">
    <a class="current">What We Do</a><a>Media Services</a><a>TV Resources</a><a>Client Portfolio</a><a>Blog</a><a>About Us</a>
  </nav>
</header>

<section class="abs hero">
  <svg class="abs hero-arrow" style="left:18px" width="24" height="52" viewBox="0 0 24 52"><polyline points="22,2 2,26 22,50" fill="none" stroke="#fff" stroke-width="2"/></svg>
  <svg class="abs hero-arrow" style="left:952px" width="24" height="52" viewBox="0 0 24 52"><polyline points="2,2 22,26 2,50" fill="none" stroke="#fff" stroke-width="2"/></svg>

  <div class="abs video">
    <div class="abs video-frame" role="img" aria-label="Video still of the two agency founders standing in front of a wall of studio monitors"></div>
    <div class="abs video-bar">
      <div class="progress"><i></i></div>
      <svg style="position:absolute;left:12px;top:7px" width="8" height="9" viewBox="0 0 8 9"><polygon points="0,0 8,4.5 0,9" fill="#ddd"/></svg>
      <svg style="position:absolute;left:28px;top:7px" width="10" height="9" viewBox="0 0 10 9"><polygon points="0,3 3,3 6,0 6,9 3,6 0,6" fill="#ddd"/></svg>
      <span class="video-time">0:03 / 1:33</span>
      <svg style="position:absolute;left:392px;top:7px" width="70" height="9" viewBox="0 0 70 9" fill="none" stroke="#ddd"><circle cx="4" cy="4.5" r="3.5"/><circle cx="22" cy="4.5" r="3"/><rect x="35" y="1" width="9" height="7"/><rect x="51" y="1" width="8" height="7"/><polyline points="63,3 63,1 66,1"/><polyline points="69,6 69,8 66,8"/></svg>
    </div>
  </div>

  <form class="abs lead-form">
    <div class="abs form-head">Drive Your<br>Business Growth</div>
    <div class="abs form-body">
      <svg class="field-icon" style="top:21px" width="12" height="12" viewBox="0 0 12 12" fill="#888"><circle cx="6" cy="3.5" r="3"/><path d="M0 12c0-4 3-5.5 6-5.5s6 1.5 6 5.5z"/></svg>
      <div class="field" style="top:20px">Name</div>
      <svg class="field-icon" style="top:53px" width="12" height="12" viewBox="0 0 12 12" fill="#888"><rect x="0" y="2" width="12" height="4" rx="2"/><rect x="2" y="6" width="8" height="5"/></svg>
      <div class="field" style="top:52px">Phone Number</div>
      <svg class="field-icon" style="top:86px" width="12" height="10" viewBox="0 0 12 10"><rect x="0" y="0" width="12" height="10" fill="#888"/><polyline points="0,0 6,5 12,0" fill="none" stroke="#fff"/></svg>
      <div class="field" style="top:85px">E-mail</div>
      <svg class="field-icon" style="top:119px" width="12" height="11" viewBox="0 0 12 11"><polygon points="0,4 6,0 12,4 12,11 0,11" fill="#888"/><polyline points="0,4 6,8 12,4" fill="none" stroke="#fff"/></svg>
      <div class="field" style="top:118px;height:59px">Message</div>
      <div class="cta">Get a free direct response campaign audit now!</div>
    </div>
  </form>
</section>

<section class="abs client-strip" aria-label="Clients">
  <div class="client" style="left:183px">Skyline TV</div>
  <div class="client" style="left:307px">VitalPage</div>
  <div class="client" style="left:449px;font-size:12px">Harrow &amp; Finch</div>
  <div class="client" style="left:563px"><i></i>TallyPro</div>
  <div class="client" style="left:687px">RateNest</div>
  <div class="client" style="left:807px"><i></i>WallHero</div>
</section>

<h1 class="abs section-title">Direct Response Marketing Agency: What We Do</h1>

<!-- row 1 -->
<svg class="abs service-icon" style="left:106px;top:632px" viewBox="0 0 24 26" fill="none" stroke="#6b6b6b" stroke-width="1.5"><path d="M3 1h13l5 5v19H3z"/><line x1="7" y1="9" x2="17" y2="9"/><line x1="7" y1="13" x2="17" y2="13"/><line x1="7" y1="17" x2="17" y2="17"/><line x1="7" y1="21" x2="14" y2="21"/></svg>
<div class="abs service-title" style="left:141px;top:642px">Media Buying Strategy</div>
<p class="abs service-text" style="left:141px;top:670px">One direct response company in the television industry is leading the charge to provide clients with an integrated, multi-channel direct response media buying strategy. That company is Brantlow Media/</p>

<svg class="abs service-icon" style="left:385px;top:632px" viewBox="0 0 28 26" width="28" fill="none" stroke="#6b6b6b" stroke-width="1.5"><rect x="1" y="6" width="26" height="19" rx="1"/><rect x="4" y="9" width="16" height="13" fill="#6b6b6b"/><line x1="9" y1="6" x2="5" y2="1"/><line x1="19" y1="6" x2="23" y2="1"/><circle cx="23.5" cy="12" r="1"/></svg>
<div class="abs service-title" style="left:424px;top:642px">Direct Response Television</div>
<p class="abs service-text" style="left:424px;top:670px">We integrate all the key mediums that comprise an effective direct response media buy, including DRTV - direct response television, online, print and radio; to ensure the success of the client's direct response media campaign.</p>

<svg class="abs service-icon" style="left:673px;top:632px" viewBox="0 0 24 26" fill="none" stroke="#6b6b6b" stroke-width="1.5"><rect x="7" y="1" width="15" height="18"/><rect x="4" y="4" width="15" height="18" fill="#fff"/><rect x="1" y="7" width="15" height="18" fill="#fff"/><line x1="4" y1="12" x2="13" y2="12"/><line x1="4" y1="16" x2="13" y2="16"/><line x1="4" y1="20" x2="13" y2="20"/></svg>
<div class="abs service-title" style="left:707px;top:642px">DRTV Media Testing and Analysis</div>
<p class="abs service-text" style="left:707px;top:670px">As a direct response agency, our staff works closely with our clients, guiding them through all stages of the media buying process, from DRTV media testing and analysis, through roll-out.</p>

<div class="abs rule-v" style="left:353px;top:632px;height:136px"></div>
<div class="abs rule-v" style="left:631px;top:632px;height:136px"></div>
<div class="abs rule-h" style="left:103px;top:785px;width:232px"></div>
<div class="abs rule-h" style="left:372px;top:785px;width:240px"></div>
<div class="abs rule-h" style="left:650px;top:785px;width:250px"></div>

<!-- row 2 -->
<svg class="abs service-icon" style="left:106px;top:816px" viewBox="0 0 26 22" width="26" fill="none" stroke="#6b6b6b" stroke-width="3.5"><polyline points="2,11 9,18 24,3"/></svg>
<div class="abs service-title" style="left:141px;top:823px">Direct Results</div>
<p class="abs service-text" style="left:141px;top:851px">Our approach enables Brantlow to deliver direct response media buys that lead to direct results.</p>

<svg class="abs service-icon" style="left:385px;top:814px" viewBox="0 0 28 26" width="28" fill="none" stroke="#6b6b6b" stroke-width="1.5"><rect x="1" y="1" width="26" height="18" rx="1"/><rect x="4" y="4" width="20" height="12" fill="#6b6b6b"/><line x1="14" y1="19" x2="14" y2="24"/><line x1="8" y1="25" x2="20" y2="25"/></svg>
<div class="abs service-title" style="left:424px;top:823px">Advertising Campaign</div>
<p class="abs service-text" style="left:424px;top:851px;width:170px">We know the 'ins' and 'outs' of maximizing the impact of a television direct response advertising campaign.</p>

<svg class="abs service-icon" style="left:669px;top:816px" viewBox="0 0 30 22" width="30" fill="none" stroke="#6b6b6b" stroke-width="1.5"><rect x="1" y="1" width="28" height="20" rx="1"/><circle cx="9" cy="9" r="3" fill="#6b6b6b"/><path d="M4 17c0-3 2.5-4 5-4s5 1 5 4z" fill="#6b6b6b"/><line x1="17" y1="7" x2="26" y2="7"/><line x1="17" y1="11" x2="26" y2="11"/><line x1="17" y1="15" x2="24" y2="15"/></svg>
<div class="abs service-title" style="left:707px;top:823px">Brantlow Media's Professionals</div>
<p class="abs service-text" style="left:707px;top:851px">The caliber of our direct response media buying performance is why marketers depend on Brantlow Media's professionals, campaign after campaign.</p>

<div class="abs rule-v" style="left:353px;top:805px;height:118px"></div>
<div class="abs rule-v" style="left:631px;top:805px;height:118px"></div>
<div class="abs rule-h" style="left:103px;top:940px;width:232px"></div>
<div class="abs rule-h" style="left:372px;top:940px;width:240px"></div>
<div class="abs rule-h" style="left:650px;top:940px;width:250px"></div>

<!-- row 3 -->
<svg class="abs service-icon" style="left:108px;top:970px" viewBox="0 0 24 24" fill="#6b6b6b"><polygon points="2,1 10,1 7,4 12,9 9,12 4,7 1,10"/><polygon points="22,23 14,23 17,20 12,15 15,12 20,17 23,14"/></svg>
<div class="abs service-title" style="left:141px;top:978px">Service</div>
<p class="abs service-text" style="left:141px;top:1006px">Service to our clients is our top priority.</p>

<svg class="abs service-icon" style="left:389px;top:968px" viewBox="0 0 22 26" width="22" fill="none" stroke="#6b6b6b" stroke-width="1.5"><rect x="1" y="3" width="20" height="22" rx="1"/><rect x="6" y="1" width="10" height="4" fill="#6b6b6b"/><polyline points="6,15 9,18 16,10" stroke-width="2.2"/></svg>
<div class="abs service-title" style="left:424px;top:978px">DRTV Media Buying Results</div>
<p class="abs service-text" style="left:424px;top:1006px;width:170px">Clients receive drtv media buying results that are measurable, specific and immediate.</p>

<div class="abs rule-v" style="left:353px;top:960px;height:84px"></div>
<div class="abs rule-v" style="left:631px;top:960px;height:84px"></div>

<footer class="abs site-footer">
  <div>drtv home | about us | key management | services | direct response television | drtv infomercial | online direct response | radio direct response</div>
  <div>print direct response | drtv lead generation | branded drtv | senior marketing specialist | media buying services | television media buying</div>
  <div>media buyer planning | reporting &amp; analysis | case studies | resources | client portfolio | past articles | contact us | site map</div>
  <div>Brantlow Interactive | Multi-Channel Direct Response | Infomercial</div>
  <div class="marks">Multi-Channel Direct Response are trademarks of Brantlow, Brantlow Media and Brantlow Interactive.</div>
</footer>

</body>
</html>
```